NEW Escape Room. Fun, Dark and Mysterious.

Escape Room Website. Bookings and scheduling of appointments will be organised with Bolkit through the site. Most appointments will be created online through the booking system with some payments coming through in person by drop-ins. Groups will be from 2 - 8 people with a sliding scale of prices. We will start with one game playable and one saying coming soon. We will also eventually have 4 games up and running at once so will need it to be able to expand. We don't have any images of the rooms because it all relies heavily on mystery. Appointments are each 1 hour long with 30 minutes in between.

Target Market(s)

15-35 year olds

Coding

Coded - Design and coding required

Number of Pages Required

5+ page

Font styles to use
Decorative

Colors

Designer to choose colors to be used in the design.

Requirements
Must have
• Graphics showing what an escape room is.
• Page for About - What is an escape room
• Page for Games - Showing each of the different games which can be played with links to booking page. We have one game to start - the tailor's shadows. A victorian doctors office and serial killers. Then a game coming soon which is aztec/mayan/jungle/captain Worrel feel.
• FAQ Page
Nice to have
• Graphics for multiple players ie 2 players, 3 players, 4 players etc
• Dark and Mysterious feel.
• Inspiration from Cipher Vault, Lockwise Hall, Puzzle Harbor
Should not have
• Cartoony/childish. Pink.
• Not bloody or dripping letters etc - not cliche.
• Not horror themed.

```html
<!DOCTYPE html>
<html lang="en">
<head>
<meta charset="utf-8">
<title>Hollow Key Escape Room</title>
<link rel="stylesheet" href="https://fonts.googleapis.com/css2?family=Oswald:wght@500;600&family=Lato:ital,wght@0,400;0,700;1,400&display=swap">
<style>
:root{
  --rust:#a9521f;
  --rust-dark:#8e4418;
  --btn-a:#a9521f;
  --btn-b:#cf8a4a;
  --blob:#c98142;
  --ink:#262626;
  --muted:#6e6e6e;
  --field:#ebebeb;
  --panel:#f1f1f1;
  --white:#ffffff;
  --black:#0d0d0d;
}
*{box-sizing:border-box;margin:0;padding:0}
html,body{width:1200px;height:3805px;overflow:hidden;background:var(--white)}
body{position:relative;font-family:"Lato",sans-serif;color:var(--ink)}
.abs{position:absolute}
.heading{font-family:"Oswald",sans-serif;font-weight:600;color:var(--ink);line-height:1}
.btn{position:absolute;display:flex;align-items:center;justify-content:center;color:var(--white);font-size:13px;letter-spacing:.5px;text-transform:uppercase;background:linear-gradient(90deg,var(--btn-a),var(--btn-b))}
.photo{position:absolute}

/* hero */
.hero-photo{left:525px;top:0;width:675px;height:638px;background:linear-gradient(135deg,#2d2620,#4a3a2c 45%,#1c1712)}
.nav{position:absolute;top:29px;left:585px;display:flex;font-size:11px;color:var(--white);letter-spacing:.3px}
.nav span{margin-right:30px;position:relative}
.nav .active::after{content:"";position:absolute;left:50%;top:18px;width:5px;height:5px;margin-left:-2px;background:var(--btn-b);transform:rotate(45deg)}
.brand{left:160px;top:40px;width:120px;display:flex;align-items:center;gap:6px;font-family:"Oswald",sans-serif;font-weight:600;font-size:18px;color:var(--ink)}
.brand i{width:12px;height:12px;background:var(--rust);display:block}
.hero-frame{left:148px;top:180px;width:30px;height:337px;border:1px solid #bdbdbd;border-right:none}
.hero-box{left:163px;top:155px;width:412px;height:414px;background:var(--rust);color:var(--white)}
.hero-box h1{position:absolute;left:23px;top:110px;font-family:"Oswald",sans-serif;font-weight:600;font-size:50px;line-height:1}
.hero-box .sub{position:absolute;left:23px;top:172px;font-style:italic;font-size:21px;line-height:1.2}
.hero-box p{position:absolute;left:23px;top:216px;width:350px;font-size:12.5px;line-height:22px}
.hero-box .outline-btn{position:absolute;left:25px;top:303px;width:119px;height:36px;border:1px solid var(--white);display:flex;align-items:center;justify-content:center;font-size:12.5px;letter-spacing:.5px}
.hero-side{left:575px;top:198px;width:15px;height:334px;border:1px solid #6b4a33;border-left:none}
.hero-corner{left:163px;top:517px;width:97px;height:52px;border-top:1px solid #d9a27c;border-right:1px solid #d9a27c}
.dots{left:550px;top:602px;display:flex;gap:9px}
.dots span{width:22px;height:2px;background:#cfcfcf}
.dots span:first-child{background:var(--btn-b)}

/* about */
.center{left:0;width:1200px;text-align:center}
.about-title{top:710px;font-size:52px}
.about-sub{top:765px;font-size:24px;line-height:1.1;color:var(--rust)}
.about-text{left:360px;top:812px;width:480px;text-align:center;font-size:11.5px;line-height:22.5px;color:var(--muted)}

/* how */
.how-photo{left:0;top:1032px;width:600px;height:450px;background:linear-gradient(120deg,#15120f,#3a2a20 50%,#17110d)}
.how-panel{left:600px;top:1032px;width:600px;height:450px;background:var(--rust);color:var(--white)}
.how-frame{left:570px;top:1090px;width:30px;height:240px;border:1px solid #a86a42;border-right:none}
.how-panel h2{position:absolute;left:55px;top:58px;font-family:"Oswald",sans-serif;font-weight:600;font-size:50px;line-height:1}
.how-panel p{position:absolute;left:55px;width:360px;font-size:11.5px;line-height:22.5px}
.feature{position:absolute;top:318px;width:140px;text-align:center;font-size:12.5px;line-height:19px}
.feature svg{display:block;margin:0 auto 10px}

/* games */
.guide{width:1px;background:#e6e6e6}
.blob{border-radius:50%;background:var(--blob)}
.game-card{background:var(--white);box-shadow:0 2px 10px rgba(0,0,0,.12);padding:26px 31px}
.game-card h3{font-family:"Oswald",sans-serif;font-weight:600;font-size:31px;color:var(--rust);line-height:1.1}
.game-card p{margin-top:10px;font-size:11.5px;line-height:22.5px;color:var(--muted);width:285px}
.meta{display:flex;align-items:center;margin-top:12px;font-size:11px;color:var(--muted);white-space:nowrap}
.meta span{display:flex;align-items:center;gap:5px;margin-right:12px}
.meta span:last-child{margin-right:0}
.stars{display:flex;gap:6px;margin-top:10px}
.game-card a{display:inline-block;margin-top:12px;font-size:12.5px;font-weight:700;color:var(--rust);text-decoration:underline}

/* who */
.who{left:0;top:2480px;width:1200px;height:451px;background:var(--rust)}
.who h2{position:absolute;left:0;width:1200px;top:26px;text-align:center;font-size:52px;color:var(--white)}
.who-card{position:absolute;background:var(--panel);text-align:center}
.who-card h3{font-family:"Oswald",sans-serif;font-weight:600;font-size:24px;line-height:1.2;margin-top:6px;letter-spacing:.5px}
.who-card p{font-size:11.5px;line-height:22.5px;color:var(--muted);margin:10px auto 0;width:225px}
.who-card .btn{position:static;width:120px;height:36px;margin:12px auto 0}
.who-card svg{display:block;margin:24px auto 0}

/* contact */
.contact-title{top:3004px;font-size:52px}
.rule{left:572px;top:3064px;width:56px;height:2px;background:var(--rust)}
.field{position:absolute;background:var(--field);font-size:11.5px;color:#9a9a9a;padding:14px 17px}

/* footer */
.footer{left:0;top:3469px;width:1200px;height:336px;background:var(--rust);color:var(--white)}
.footer h4{position:absolute;top:40px;font-family:"Oswald",sans-serif;font-weight:500;font-size:19px;letter-spacing:.3px}
.links{position:absolute;top:103px;font-size:12px;line-height:26px}
.links li{list-style:none}
.links li::before{content:"›";margin-right:6px}
.contact-row{position:absolute;display:flex;gap:14px;font-size:12px;line-height:19px}
.social{position:absolute;top:3656px;display:flex;gap:28px;left:612px}
.social span{width:20px;height:20px;border:2px solid var(--white);border-radius:50%}
.footer-mark{left:836px;top:3469px;width:203px;height:292px;background:var(--black);display:flex;align-items:center;justify-content:center;gap:8px;font-family:"Oswald",sans-serif;font-weight:600;font-size:24px;color:var(--btn-b)}
.footer-mark i{width:14px;height:14px;background:var(--btn-b);display:block}
.footer-line{left:0;top:3761px;width:1200px;height:1px;background:#c07a4b}
.copy{left:0;width:1200px;top:3778px;text-align:center;font-size:11px;color:var(--white)}
</style>
</head>
<body>

<!-- hero -->
<div class="photo hero-photo" role="img" aria-label="Photo of two players searching for clues in a dimly lit escape room"></div>
<nav class="nav">
  <span class="active">HOME</span><span>ABOUT US</span><span>GAMES</span><span>HOW IT WORKS</span><span>FAQ</span><span>CONTACT US</span>
</nav>
<div class="abs brand"><i></i>Hollow Key</div>
<div class="abs hero-frame"></div>
<div class="abs hero-side"></div>
<section class="abs hero-box">
  <h1>Hollow Key</h1>
  <div class="sub">Escap Room</div>
  <p>Lorem Ipsum is simply dummy text of the printing and typesetting industry. Lorem Ipsum has been the industry's standard dummy text ever since the 1500s.</p>
  <div class="outline-btn">BOOK NOW</div>
</section>
<div class="abs hero-corner"></div>
<div class="abs dots"><span></span><span></span><span></span></div>

<!-- about -->
<h2 class="abs center heading about-title">About Us</h2>
<div class="abs center about-sub">Escap Room</div>
<p class="abs about-text">Lorem Ipsum is simply dummy text of the printing and typesetting industry. Lorem Ipsum has been the industry's standard dummy text ever since the 1500s.Lorem Ipsum is simply dummy text of the printing and typesetting industry. Lorem Ipsum has been the industry's standard dummy text ever since the 1500s.</p>
<div class="btn" style="left:539px;top:919px;width:120px;height:36px">BOOK NOW</div>

<!-- how it works -->
<div class="photo how-photo" role="img" aria-label="Photo of players solving puzzles in a dark kitchen themed room"></div>
<section class="abs how-panel">
  <h2>How it works</h2>
  <p style="top:124px">You and your friends are starring in your own themed adventure. As the clock counts down, you use logic and teamwork to find clues, solve puzzles, and escape before time runs out!</p>
  <p style="top:195px">We look forword to locking you up! keep reading to see our roomes.</p>
  <svg class="abs" style="left:213px;top:258px" width="32" height="20" viewBox="0 0 32 20"><path d="M2 2l14 14L30 2" fill="none" stroke="#fff" stroke-width="1.5"/><path d="M6 2l10 10L26 2" fill="none" stroke="#fff" stroke-width="1" opacity=".6"/></svg>
  <div class="feature" style="left:16px">
    <svg width="40" height="36" viewBox="0 0 40 36" fill="none" stroke="#fff" stroke-width="1.6"><circle cx="13" cy="10" r="7"/><circle cx="27" cy="10" r="7"/><path d="M2 34v-5a8 8 0 0 1 8-8h6a8 8 0 0 1 8 8v5zM20 22a8 8 0 0 1 4-1h6a8 8 0 0 1 8 8v5H24"/></svg>
    2 to 6&nbsp; Players</div>
  <div class="feature" style="left:150px">
    <svg width="40" height="40" viewBox="0 0 40 40" fill="none" stroke="#fff" stroke-width="1.8"><circle cx="20" cy="20" r="17"/><path d="M20 9v11l7 6"/></svg>
    45 Minutes of<br>Gameplay</div>
  <div class="feature" style="left:304px">
    <svg width="40" height="40" viewBox="0 0 40 40" fill="none" stroke="#fff" stroke-width="1.8"><circle cx="28" cy="12" r="8"/><path d="M22 18L4 36M9 31l4 4M13 27l4 4"/></svg>
    Tons of Adventures to<br>choose from</div>
</section>
<div class="abs how-frame"></div>

<!-- games -->
<div class="abs guide" style="left:343px;top:1482px;height:998px"></div>
<div class="abs guide" style="left:1005px;top:1900px;height:580px"></div>

<div class="abs blob" style="left:161px;top:1758px;width:162px;height:170px;border-radius:55% 45% 50% 50%"></div>
<div class="photo" style="left:214px;top:1599px;width:451px;height:300px;background:linear-gradient(135deg,#3a2a1e,#6d4a2c 50%,#1f3a6e)" role="img" aria-label="Photo of players in blue suits working a safe in a Victorian office room"></div>
<article class="abs game-card" style="left:630px;top:1621px;width:375px;height:250px">
  <h3>Tailor's Shadows</h3>
  <p>Paris in the winter of 1822.&nbsp; The nights are long and unseasonably cold.&nbsp; The streets are dark and uncharacteristically quiet.</p>
  <div class="meta">
    <span><svg width="18" height="16" viewBox="0 0 18 16" fill="none" stroke="#c98142" stroke-width="1.3"><rect x="1" y="2" width="16" height="13"/><path d="M1 6h16M5 0v4M13 0v4"/></svg>Appointment</span>
    <span><svg width="16" height="16" viewBox="0 0 16 16" fill="none" stroke="#c98142" stroke-width="1.3"><circle cx="8" cy="8" r="7"/><path d="M8 4v4l3 2"/></svg>8:00 am To 9:pm</span>
    <span><svg width="18" height="16" viewBox="0 0 18 16" fill="none" stroke="#c98142" stroke-width="1.3"><circle cx="7" cy="5" r="4"/><path d="M1 15a6 6 0 0 1 12 0zM11 2a4 4 0 0 1 2 7 5 5 0 0 1 4 6"/></svg>2-3 Players</span>
  </div>
  <div class="stars">
    <svg width="96" height="16" viewBox="0 0 96 16"><g fill="#9a9a9a"><path id="s" d="M8 1l2.1 4.5 4.9.6-3.6 3.4.9 4.9L8 12l-4.3 2.4.9-4.9L1 6.1l4.9-.6z"/><use href="#s" x="20"/><use href="#s" x="40"/><use href="#s" x="60"/></g><use href="#s" x="80" fill="none" stroke="#9a9a9a"/></svg>
  </div>
  <a>Book Now</a>
</article>

<div class="abs blob" style="left:938px;top:2000px;width:102px;height:122px"></div>
<div class="photo" style="left:646px;top:2029px;width:375px;height:376px;background:linear-gradient(150deg,#3d0f0a,#8a2a14 45%,#5a3a1c)" role="img" aria-label="Photo of players opening a glowing treasure chest in a jungle tomb room"></div>
<article class="abs game-card" style="left:343px;top:2124px;width:377px;height:248px">
  <h3>Jade Serpent's Tomb</h3>
  <p>Paris in the winter of 1822.&nbsp; The nights are long and unseasonably cold.&nbsp; The streets are dark and uncharacteristically quiet.</p>
  <div class="meta">
    <span><svg width="18" height="16" viewBox="0 0 18 16" fill="none" stroke="#c98142" stroke-width="1.3"><rect x="1" y="2" width="16" height="13"/><path d="M1 6h16M5 0v4M13 0v4"/></svg>Appointment</span>
    <span><svg width="16" height="16" viewBox="0 0 16 16" fill="none" stroke="#c98142" stroke-width="1.3"><circle cx="8" cy="8" r="7"/><path d="M8 4v4l3 2"/></svg>8:00 am To 9:pm</span>
    <span><svg width="18" height="16" viewBox="0 0 18 16" fill="none" stroke="#c98142" stroke-width="1.3"><circle cx="7" cy="5" r="4"/><path d="M1 15a6 6 0 0 1 12 0zM11 2a4 4 0 0 1 2 7 5 5 0 0 1 4 6"/></svg>2-3 Players</span>
  </div>
  <div class="stars">
    <svg width="96" height="16" viewBox="0 0 96 16"><g fill="#9a9a9a"><path id="s2" d="M8 1l2.1 4.5 4.9.6-3.6 3.4.9 4.9L8 12l-4.3 2.4.9-4.9L1 6.1l4.9-.6z"/><use href="#s2" x="20"/><use href="#s2" x="40"/><use href="#s2" x="60"/></g><use href="#s2" x="80" fill="none" stroke="#9a9a9a"/></svg>
  </div>
  <a>Book Now</a>
</article>

<!-- who can play -->
<section class="abs who">
  <h2 class="heading" style="color:var(--white)">Who Can Play</h2>
  <div class="who-card" style="left:161px;top:136px;width:263px;height:269px">
    <svg width="44" height="50" viewBox="0 0 44 50" fill="none" stroke="#c98142" stroke-width="1.6"><circle cx="12" cy="6" r="4"/><circle cx="32" cy="14" r="3.5"/><path d="M6 14h12v16h-3v18H9V30H6zM27 22h10v12h-2v14h-6V34h-2z"/></svg>
    <h3>Family</h3>
    <p>Lorem Ipsum is simply dummy text of the industry. Lorem Ipsum has been the industry's standard dummy text.</p>
    <div class="btn">BOOK NOW</div>
  </div>
  <div class="who-card" style="left:468px;top:121px;width:264px;height:299px">
    <svg width="54" height="54" viewBox="0 0 54 54" fill="none" stroke="#c98142" stroke-width="1.6"><rect x="2" y="28" width="50" height="22"/><rect x="10" y="4" width="10" height="24"/><rect x="22" y="4" width="10" height="24"/><rect x="34" y="4" width="10" height="24"/><path d="M8 38h38M8 42h38" stroke-dasharray="3 3"/></svg>
    <h3>Corporate</h3>
    <p>Lorem Ipsum is simply dummy text of the printing and typesetting industry. Lorem Ipsum has been the industry's standard dummy text.</p>
    <div class="btn">BOOK NOW</div>
  </div>
  <div class="who-card" style="left:776px;top:136px;width:263px;height:269px">
    <svg width="54" height="50" viewBox="0 0 54 50" fill="none" stroke="#c98142" stroke-width="1.6"><circle cx="20" cy="8" r="5"/><circle cx="34" cy="8" r="5"/><circle cx="12" cy="24" r="5"/><circle cx="27" cy="24" r="5"/><circle cx="42" cy="24" r="5"/><path d="M2 46a10 10 0 0 1 20 0zM17 46a10 10 0 0 1 20 0zM32 46a10 10 0 0 1 20 0z"/></svg>
    <h3>Friends</h3>
    <p>Lorem Ipsum is simply dummy text of the industry. Lorem Ipsum has been the industry's standard dummy text.</p>
    <div class="btn">BOOK NOW</div>
  </div>
</section>

<!-- contact -->
<h2 class="abs center heading contact-title">Contact Us</h2>
<div class="abs rule"></div>
<div class="field" style="left:278px;top:3108px;width:299px;height:45px">Name*</div>
<div class="field" style="left:622px;top:3108px;width:300px;height:45px">Phone*</div>
<div class="field" style="left:278px;top:3176px;width:644px;height:45px">E-mail*</div>
<div class="field" style="left:278px;top:3244px;width:644px;height:89px;padding-top:11px">Message*</div>
<div class="btn" style="left:539px;top:3356px;width:120px;height:37px">SEND</div>

<!-- footer -->
<footer class="abs footer">
  <h4 style="left:161px">Quick Links</h4>
  <ul class="links" style="left:161px;top:102px"><li>HOME</li><li>ABOUT US</li><li>GAMES</li><li>HOW IT WORKS</li><li>FAQ</li><li>CONTACT US</li></ul>
  <h4 style="left:387px">Get In Touch</h4>
  <div class="contact-row" style="left:387px;top:103px">
    <svg width="18" height="22" viewBox="0 0 18 22"><path d="M9 1a7 7 0 0 0-7 7c0 5 7 13 7 13s7-8 7-13a7 7 0 0 0-7-7z" fill="#fff"/><circle cx="9" cy="8" r="2.8" fill="#a9521f"/></svg>
    <span>123 - Lorem ipsum is dummy<br>text and dynemic text.</span></div>
  <div class="contact-row" style="left:387px;top:152px">
    <svg width="18" height="18" viewBox="0 0 18 18"><path d="M4 1l3 4-2 2a11 11 0 0 0 6 6l2-2 4 3-2 3C8 17 1 10 1 3z" fill="#fff"/></svg>
    <span>123 456 7890</span></div>
  <div class="contact-row" style="left:387px;top:191px">
    <svg width="20" height="14" viewBox="0 0 20 14" fill="none" stroke="#fff" stroke-width="1.5"><rect x="1" y="1" width="18" height="12"/><path d="M1 1l9 7 9-7"/></svg>
    <span>info@hollowkeyrooms.com</span></div>
  <h4 style="left:612px">Games</h4>
  <ul class="links" style="left:612px;top:102px"><li>Tailor's Shadows</li><li>Jade Serpent's Tomb</li></ul>
</footer>
<div class="social"><span></span><span></span><span></span></div>
<div class="abs footer-mark"><i></i>Hollow Key</div>
<div class="abs footer-line"></div>
<div class="abs copy">©Escape Room - 2020 All Rights Reserved.</div>

</body>
</html>
```